Lumen Harbor Business Card Design Project

We have recently rebranded and would like to design new business cards that incorporate the corporate logo - double sided cards with corporate logo on one side and contact details on the other

Target Market(s)

Sophisticated and high net worth investors and finance industry professionals

Industry/Entity Type

Funds Management

Contact Information for Business Card

The card should prominently feature the company name and logo. Other details will be standard contact details for each staff member - name, address, phone, email, website

Colors
0054AA
0677BA
7BADD7
CADEEF
E8F1F8

Requirements
Must have
• Double-sided design with one side prominently featuring the corporate logo and the other side with all standard contact details

```html
<!DOCTYPE html>
<html lang="en">
<head>
<meta charset="utf-8">
<title>Lumen Harbor – Business Card</title>
<link rel="stylesheet" href="https://fonts.googleapis.com/css2?family=Cinzel:wght@500&family=Montserrat:wght@400;600&display=swap">
<style>
  :root {
    --navy: #234b7c;
    --navy-deep: #1e4473;
    --white: #ffffff;
    --page: #e8ecf1;
    --soft: #cadeef;
  }
  * { box-sizing: border-box; margin: 0; padding: 0; }
  html, body { width: 1200px; height: 1200px; overflow: hidden; }
  body {
    background: var(--page);
    font-family: "Montserrat", sans-serif;
    display: flex;
    flex-direction: column;
    align-items: center;
    justify-content: center;
    gap: 52px;
  }
  .card {
    width: 900px;
    height: 514px;
    border-radius: 36px;
    overflow: hidden;
    position: relative;
    box-shadow: 0 6px 22px rgba(20, 40, 70, 0.18);
  }

  /* Front: contact side */
  .card--front { background: var(--white); }
  .front__brand {
    position: absolute;
    top: 0; left: 0; right: 0;
    height: 230px;
    display: flex;
    align-items: center;
    justify-content: center;
  }
  .wordmark {
    font-family: "Cinzel", serif;
    font-weight: 500;
    letter-spacing: 3px;
    color: var(--navy);
    font-size: 58px;
  }
  .front__rule {
    position: absolute;
    left: 0; right: 0;
    top: 246px;
    height: 6px;
    background: var(--navy);
  }
  .front__band {
    position: absolute;
    left: 0; right: 0;
    top: 266px; bottom: 0;
    background: linear-gradient(100deg, var(--navy-deep), var(--navy) 55%, var(--navy-deep));
    color: var(--white);
    display: flex;
    align-items: center;
    justify-content: space-between;
    padding: 0 60px 0 70px;
  }
  .person {
    border-left: 6px solid var(--white);
    padding-left: 16px;
  }
  .person__name {
    font-weight: 600;
    font-size: 40px;
    letter-spacing: 0.5px;
    line-height: 1.05;
  }
  .person__role {
    font-size: 20px;
    letter-spacing: 1px;
    margin-top: 4px;
  }
  .contact { list-style: none; font-size: 17px; line-height: 1.25; }
  .contact li {
    display: flex;
    align-items: flex-start;
    gap: 12px;
    margin: 6px 0;
  }
  .contact svg { width: 18px; height: 18px; flex: none; margin-top: 1px; fill: var(--white); }

  /* Back: brand side */
  .card--back {
    background: linear-gradient(120deg, var(--navy-deep), #2a5689 50%, var(--navy-deep));
    display: flex;
    align-items: center;
    justify-content: center;
  }
  .card--back .wordmark {
    color: var(--white);
    font-size: 76px;
  }
</style>
</head>
<body>

  <section class="card card--front" aria-label="Business card, contact side">
    <div class="front__brand">
      <span class="wordmark">Lumen Harbor</span>
    </div>
    <div class="front__rule"></div>
    <div class="front__band">
      <div class="person">
        <p class="person__name">ELLIOT MARSH</p>
        <p class="person__role">CEO | FOUNDER</p>
      </div>
      <ul class="contact">
        <li>
          <svg viewBox="0 0 24 24" aria-hidden="true"><path d="M6.6 10.8a15.1 15.1 0 0 0 6.6 6.6l2.2-2.2a1 1 0 0 1 1-.25 11.4 11.4 0 0 0 3.6.57 1 1 0 0 1 1 1V20a1 1 0 0 1-1 1A17 17 0 0 1 3 4a1 1 0 0 1 1-1h3.5a1 1 0 0 1 1 1c0 1.25.2 2.45.57 3.57a1 1 0 0 1-.25 1z"/></svg>
          <span>+02 5550 1947</span>
        </li>
        <li>
          <svg viewBox="0 0 24 24" aria-hidden="true"><path d="M12 2a10 10 0 1 0 0 20 10 10 0 0 0 0-20zm6.9 6h-3a15.6 15.6 0 0 0-1.3-3.9A8 8 0 0 1 18.9 8zM12 4c.8 1.2 1.5 2.5 1.9 4h-3.8c.4-1.5 1.1-2.8 1.9-4zM4.3 14a8 8 0 0 1 0-4h3.4a16 16 0 0 0 0 4zm.8 2h3a15.6 15.6 0 0 0 1.3 3.9A8 8 0 0 1 5.1 16zm3-8h-3a8 8 0 0 1 4.3-3.9A15.6 15.6 0 0 0 8.1 8zM12 20c-.8-1.2-1.5-2.5-1.9-4h3.8c-.4 1.5-1.1 2.8-1.9 4zm2.3-6H9.7a14.7 14.7 0 0 1 0-4h4.6a14.7 14.7 0 0 1 0 4zm.3 5.9a15.6 15.6 0 0 0 1.3-3.9h3a8 8 0 0 1-4.3 3.9zm1.7-5.9a16 16 0 0 0 0-4h3.4a8 8 0 0 1 0 4z"/></svg>
          <span>www.lumen-harbor.com</span>
        </li>
        <li>
          <svg viewBox="0 0 24 24" aria-hidden="true"><path d="M2 5h20v14H2zm2 2v.5l8 5.5 8-5.5V7zm0 2.9V17h16V9.9l-8 5.5z"/></svg>
          <span>invest@lumen-harbor.com</span>
        </li>
        <li>
          <svg viewBox="0 0 24 24" aria-hidden="true"><path d="M12 2a7 7 0 0 0-7 7c0 5.2 7 13 7 13s7-7.8 7-13a7 7 0 0 0-7-7zm0 9.5A2.5 2.5 0 1 1 12 6.5a2.5 2.5 0 0 1 0 5z"/></svg>
          <span>Level 14 Meridian House, 42<br>Keel Street, Sydney NSW 2000</span>
        </li>
      </ul>
    </div>
  </section>

  <section class="card card--back" aria-label="Business card, brand side">
    <span class="wordmark">Lumen Harbor</span>
  </section>

</body>
</html>
```